Technical audit needs a report template

As our company runs various technical audits, we also provide findings on paper, online or in Powerpoint. For this reason we need an identity pack, which includes business cards, complimentary cards, letterhead and the likes.

Who would be up to create this stationery pack for us? We hope to receive a style for these documents, that look professional and can be easily extended.
Updates

Project Deadline Extended Reason: I would like to provide the opportunity to friended designers to submit their designs too! Added Sunday, October 9, 2016

Target Market(s)

Start-ups, scale-ups and investors

Industry/Entity Type

Investment

Contact Information for Business Card

Street: Kastelenhofweg 41
Postcode: 3614KT
City: Utrecht
Country: The Netherlands
Phone: +31 304185926
Cell Phone: +31 6 57193840
email: jorien@velmoraxis.example
website: https://velmoraxis.example

Requirements
Must have
• I don't have inspiration, should just be a slick design based on the logo provided.
Nice to have
• Logo could be on the back of the card?
Should not have
• Should not use different colours then the logo, or at least fit the colour scheme.

```html
<!DOCTYPE html>
<html lang="en">
<head>
<meta charset="utf-8">
<title>Velmoraxis – Envelope and Compliments Card</title>
<link rel="stylesheet" href="https://fonts.googleapis.com/css2?family=Roboto:wght@300;400;700&display=swap">
<style>
  :root {
    --bg: #ececec;
    --paper: #f4f4f4;
    --flap: #3a3a3a;
    --blue: #4aaedc;
    --blue-deep: #1f8fc4;
    --ink: #2e2e2e;
  }
  * { box-sizing: border-box; margin: 0; padding: 0; }
  html, body {
    width: 1200px; height: 795px; overflow: hidden;
    background: var(--bg);
    font-family: "Roboto", Arial, sans-serif;
    color: var(--ink);
  }
  .stationery {
    position: relative; width: 1200px; height: 795px;
  }

  /* Envelope (back view) */
  .envelope {
    position: absolute; left: 50px; top: 255px;
    width: 530px; height: 265px;
    background: var(--paper);
    box-shadow: 0 2px 6px rgba(0,0,0,.12);
  }
  .envelope__flap {
    position: absolute; left: 0; top: 0;
    width: 100%; height: 96px;
    background: var(--flap);
    border-radius: 0 0 18px 0;
    display: flex; align-items: center; justify-content: center;
  }
  .envelope__url {
    color: var(--blue); font-size: 13px; font-weight: 400; letter-spacing: .2px;
  }

  /* Compliments card */
  .comp-card {
    position: absolute; left: 620px; top: 250px;
    width: 530px; height: 275px;
    background: var(--blue);
    padding: 9px;
    box-shadow: 0 2px 6px rgba(0,0,0,.12);
  }
  .comp-card__inner {
    position: relative; width: 100%; height: 100%;
    background: var(--paper);
  }
  .comp-card__greeting {
    position: absolute; right: 22px; top: 18px;
    color: var(--blue); font-size: 20px; font-weight: 300;
  }
  .brand {
    position: absolute; left: 22px; top: 104px;
    display: flex; align-items: center; gap: 10px;
  }
  .brand__square {
    width: 30px; height: 30px; background: var(--blue-deep);
  }
  .brand__name {
    font-size: 26px; font-weight: 700; color: var(--ink); letter-spacing: .3px;
  }
  .contact {
    position: absolute; bottom: 22px;
    padding-left: 12px;
    border-left: 1.5px solid var(--blue);
    font-size: 12px; line-height: 1.4; font-weight: 400;
  }
  .contact--direct { left: 22px; }
  .contact--address { left: 250px; bottom: 110px; }
  .contact__web { color: var(--blue-deep); font-weight: 700; }
</style>
</head>
<body>
<main class="stationery">
  <section class="envelope" aria-label="Envelope back">
    <div class="envelope__flap">
      <span class="envelope__url">velmoraxis.example</span>
    </div>
  </section>

  <section class="comp-card" aria-label="Compliments card">
    <div class="comp-card__inner">
      <p class="comp-card__greeting">With compliments</p>

      <div class="brand">
        <span class="brand__square" aria-hidden="true"></span>
        <span class="brand__name">Velmoraxis</span>
      </div>

      <address class="contact contact--address">
        Kastelenhofweg 41<br>
        3614KT Utrecht<br>
        The Netherlands
      </address>

      <address class="contact contact--direct">
        +31 304185926<br>
        jorien@velmoraxis.example<br>
        <span class="contact__web">velmoraxis.example</span>
      </address>
    </div>
  </section>
</main>
</body>
</html>
```